Cannabis Security Company- Sales Flyer

Take the copy and make a sleek design- no cannabis leave or paraphernalia. Add graphic elements to the Product Offering section

```html
<!DOCTYPE html>
<html lang="en">
<head>
<meta charset="utf-8">
<title>Corelink – Sales Flyer</title>
<link href="https://fonts.googleapis.com/css2?family=Lato:wght@400;700;900&display=swap" rel="stylesheet">
<style>
  :root{
    --slate:#557a8f;
    --slate-dark:#46687b;
    --ink:#1d1d1f;
    --paper:#ffffff;
    --line:#2a2a2a;
    --grey-line:#8e8e8e;
    --photo-a:#c9d6dd;
    --photo-b:#8fa6b3;
  }
  *{box-sizing:border-box;margin:0;padding:0}
  html,body{width:905px;height:1200px;overflow:hidden;background:var(--paper);font-family:'Lato',sans-serif;color:var(--ink)}
  .flyer{position:relative;width:905px;height:1200px;background:var(--paper)}
  .hero-photo{position:absolute;left:0;top:0;width:905px;height:290px;
    background:linear-gradient(120deg,var(--photo-a) 0%,var(--photo-b) 45%,#b7c7cf 70%,var(--photo-a) 100%)}
  .hero-edge{position:absolute;left:0;top:230px;width:905px;height:80px}
  .brand{position:absolute;left:46px;top:300px;display:flex;align-items:center;gap:12px}
  .brand-mark{width:22px;height:22px;background:var(--ink)}
  .brand-name{font-size:54px;font-weight:900;letter-spacing:1px;color:var(--ink);line-height:1}
  .headline{position:absolute;left:412px;top:336px;font-size:28px;font-weight:900;line-height:1.25;text-transform:uppercase;color:var(--ink)}
  .intro{position:absolute;left:42px;top:446px;width:822px;font-size:15.5px;line-height:1.38}
  .offer-band{position:absolute;left:0;top:548px;width:905px;height:242px;background:var(--slate);color:#fff}
  .offer-title{position:absolute;left:42px;top:14px;font-size:16px;font-weight:700}
  .offer-rule{position:absolute;left:42px;top:38px;width:800px;height:1px;background:#fff}
  .offer-list{position:absolute;left:42px;top:54px;list-style:none;font-size:12.6px;line-height:18.2px}
  .offer-list li{display:flex}
  .offer-list .label{width:140px}
  .offer-list .label::before{content:"✓";margin-right:8px}
  .finance-list{position:absolute;left:90px;top:176px;list-style:none;font-size:12.6px;line-height:18.2px}
  .finance-list li::before{content:"";display:inline-block;width:8px;height:8px;border:1px solid #fff;border-radius:50%;margin-right:9px}
  .finance-list b{font-weight:700}
  .section-tag{position:absolute;left:290px;top:818px;width:325px;height:40px;background:var(--slate);color:#fff;
    font-size:19px;font-weight:700;display:flex;align-items:center;justify-content:center;box-shadow:4px 4px 0 #c8d2d8}
  .products{position:absolute;left:40px;top:880px;width:830px;display:flex;justify-content:space-between}
  .product{width:125px;text-align:center;font-size:15.5px;font-weight:700;line-height:1.25}
  .product svg{display:block;margin:0 auto 10px}
  .product .name{height:44px;display:flex;align-items:center;justify-content:center;font-weight:400}
  .rule{position:absolute;height:4px;background:var(--line)}
  .rule.grey{background:var(--grey-line);height:3px}
  .footer{position:absolute;left:0;top:1082px;width:905px;height:118px}
  .cta{position:absolute;left:42px;top:1102px;color:#fff;font-size:16px;font-weight:700}
  .contacts{position:absolute;left:0;top:1146px;width:905px;height:54px;display:flex;justify-content:center;align-items:center;gap:26px;color:#fff;font-size:16px;font-weight:700}
  .contacts .sep{width:1px;height:28px;background:#fff}
  .contacts span{display:flex;align-items:center;gap:9px}
</style>
</head>
<body>
<main class="flyer">
  <div class="hero-photo" role="img" aria-label="Photo of two hands joining circuit-board puzzle pieces"></div>
  <svg class="hero-edge" viewBox="0 0 905 80" aria-hidden="true">
    <path d="M0 24 L300 24 Q325 24 345 44 L905 44 L905 80 L0 80 Z" fill="#fff"/>
    <path d="M0 24 L300 24 Q325 24 345 44 L905 44" fill="none" stroke="#2a2a2a" stroke-width="4"/>
    <rect x="0" y="32" width="260" height="3" fill="#8e8e8e"/>
    <rect x="610" y="32" width="295" height="3" fill="#8e8e8e"/>
  </svg>

  <div class="brand"><span class="brand-mark"></span><span class="brand-name">CORELINK</span></div>
  <svg style="position:absolute;left:396px;top:294px" width="509" height="24" aria-hidden="true">
    <rect x="0" y="0" width="509" height="4" fill="#2a2a2a"/>
    <rect x="420" y="12" width="89" height="3" fill="#8e8e8e"/>
  </svg>
  <h1 class="headline">Doing what you do best-<br>running your business!</h1>

  <p class="intro">Due to the regulations put forth by the State of California, there is high cost associated with being in compliance to maintain your license and not receive fines as it pertains to security for your facility. In addition, the data intense programs with the seed-to-sale program can be a hindrance to you doing what you do best- running your business!</p>

  <section class="offer-band">
    <h2 class="offer-title">What Corelink Can Offer</h2>
    <div class="offer-rule"></div>
    <ul class="offer-list">
      <li><span class="label">Experience-</span>We have been in the it and video surveillance business for over 20 years</li>
      <li><span class="label">Compliance-</span>Our attorney helped write prop 64 and can keep you in compliance with the ever-changing regulations</li>
      <li><span class="label">Cost Savings-</span>Corelink can save you 15-30% over the competition</li>
      <li><span class="label">Speed-</span>Our solutions can be designed and implemented within days, not months</li>
      <li><span class="label">Customization-</span>Our products are architected around the business not the business around the products</li>
      <li><span class="label">Finance options-</span>Corelink offers the following options for purchase</li>
    </ul>
    <ul class="finance-list">
      <li><b>Outright purchase</b>- own your own equipment and data</li>
      <li><b>Leasing with a monthly payment</b>- prevent large outlay of cash</li>
      <li><b>Managed/cloud offering</b>- we send the gear and manage in a secure location</li>
    </ul>
  </section>

  <div class="section-tag">PRODUCT OFFERING</div>

  <div class="products">
    <div class="product">
      <svg width="118" height="118" viewBox="0 0 118 118" aria-hidden="true">
        <circle cx="56" cy="56" r="52" fill="#fff" stroke="#ddd" stroke-width="2"/>
        <path d="M56 4 A52 52 0 0 1 56 108" fill="none" stroke="#557a8f" stroke-width="6"/>
        <g fill="#1d1d1f"><rect x="30" y="46" width="46" height="18" rx="3" transform="rotate(-20 53 55)"/><rect x="64" y="62" width="6" height="18"/><rect x="58" y="78" width="22" height="6"/><circle cx="32" cy="66" r="5"/></g>
      </svg>
      <div class="name">Video<br>Surveillance</div>
    </div>
    <div class="product">
      <svg width="118" height="118" viewBox="0 0 118 118" aria-hidden="true">
        <circle cx="56" cy="56" r="52" fill="#fff" stroke="#ddd" stroke-width="2"/>
        <path d="M56 4 A52 52 0 0 1 56 108" fill="none" stroke="#557a8f" stroke-width="6"/>
        <g fill="#1d1d1f"><rect x="38" y="30" width="32" height="34" rx="2"/><path d="M32 50 L80 50 L76 80 L36 80 Z"/></g>
        <g fill="#fff"><rect x="44" y="38" width="20" height="2"/><rect x="44" y="44" width="20" height="2"/></g>
      </svg>
      <div class="name">Data Storage</div>
    </div>
    <div class="product">
      <svg width="118" height="118" viewBox="0 0 118 118" aria-hidden="true">
        <circle cx="56" cy="56" r="52" fill="#fff" stroke="#ddd" stroke-width="2"/>
        <path d="M56 4 A52 52 0 0 1 56 108" fill="none" stroke="#557a8f" stroke-width="6"/>
        <rect x="38" y="28" width="38" height="52" rx="3" fill="#1d1d1f"/>
        <path d="M57 44 L68 48 L68 58 Q68 68 57 72 Q46 68 46 58 L46 48 Z" fill="#fff"/>
        <path d="M57 49 L63 51 L63 58 Q63 64 57 66 Q51 64 51 58 L51 51 Z" fill="#1d1d1f"/>
      </svg>
      <div class="name">Data Security</div>
    </div>
    <div class="product">
      <svg width="118" height="118" viewBox="0 0 118 118" aria-hidden="true">
        <circle cx="56" cy="56" r="52" fill="#fff" stroke="#ddd" stroke-width="2"/>
        <path d="M56 4 A52 52 0 0 1 56 108" fill="none" stroke="#557a8f" stroke-width="6"/>
        <g stroke="#1d1d1f" stroke-width="2"><line x1="56" y1="56" x2="56" y2="28"/><line x1="56" y1="56" x2="56" y2="84"/><line x1="56" y1="56" x2="30" y2="44"/><line x1="56" y1="56" x2="82" y2="44"/><line x1="56" y1="56" x2="30" y2="70"/><line x1="56" y1="56" x2="82" y2="70"/></g>
        <g fill="#1d1d1f"><circle cx="56" cy="56" r="10"/><circle cx="56" cy="28" r="5"/><circle cx="56" cy="84" r="5"/><circle cx="30" cy="44" r="5"/><circle cx="82" cy="44" r="5"/><circle cx="30" cy="70" r="5"/><circle cx="82" cy="70" r="5"/></g>
      </svg>
      <div class="name">Networking</div>
    </div>
    <div class="product">
      <svg width="118" height="118" viewBox="0 0 118 118" aria-hidden="true">
        <circle cx="56" cy="56" r="52" fill="#fff" stroke="#ddd" stroke-width="2"/>
        <path d="M56 4 A52 52 0 0 1 56 108" fill="none" stroke="#557a8f" stroke-width="6"/>
        <g fill="none" stroke="#1d1d1f" stroke-width="3"><path d="M46 30 Q40 38 46 46"/><path d="M66 30 Q72 38 66 46"/><path d="M40 24 Q30 38 40 52"/><path d="M72 24 Q82 38 72 52"/></g>
        <circle cx="56" cy="38" r="5" fill="#1d1d1f"/>
        <path d="M54 42 L58 42 L62 84 L50 84 Z" fill="#1d1d1f"/>
      </svg>
      <div class="name">Wireless<br>Connectivity</div>
    </div>
  </div>

  <div class="rule grey" style="left:0;top:1050px;width:175px"></div>
  <div class="rule" style="left:0;top:1058px;width:175px;height:2px;background:#bbb"></div>
  <div class="rule" style="left:610px;top:1070px;width:295px"></div>
  <div class="rule grey" style="left:610px;top:1078px;width:295px;height:2px"></div>

  <svg class="footer" viewBox="0 0 905 118" aria-hidden="true">
    <path d="M0 0 L365 0 Q385 0 395 14 Q405 28 425 28 L905 28 L905 118 L0 118 Z" fill="#557a8f"/>
  </svg>
  <div class="cta">Call us today for a free consultation</div>
  <div class="contacts">
    <span><svg width="16" height="16" viewBox="0 0 16 16" aria-hidden="true"><circle cx="8" cy="8" r="7" fill="none" stroke="#fff" stroke-width="1.5"/><path d="M5 4 L7 6 L6 7 Q7 9 9 10 L10 9 L12 11 L10.5 12.5 Q6 12 3.5 6 Z" fill="#fff"/></svg>555-201-4830</span>
    <i class="sep"></i>
    <span><svg width="16" height="12" viewBox="0 0 16 12" aria-hidden="true"><rect x="1" y="1" width="14" height="10" fill="none" stroke="#fff" stroke-width="1.5"/><path d="M1 1 L8 7 L15 1" fill="none" stroke="#fff" stroke-width="1.5"/></svg>info@corelinksecure.com</span>
    <i class="sep"></i>
    <span><svg width="16" height="16" viewBox="0 0 16 16" aria-hidden="true"><g fill="none" stroke="#fff" stroke-width="1.4"><circle cx="8" cy="8" r="7"/><ellipse cx="8" cy="8" rx="3" ry="7"/><line x1="1" y1="8" x2="15" y2="8"/></g></svg>www.corelinksecure.com</span>
  </div>
</main>
</body>
</html>
```